Order Form Template

We are looking to develop a professional looking order form, also see attached a brochure of our solution to see how nice it is from the brochure, I also attached devices logos. I would like to have the devices nd plans in multiple lines and quantity and price and total price. also leave a space below for a policy of billing and cancellation which we will add ourself later.

```html
<!DOCTYPE html>
<html lang="en">
<head>
<meta charset="utf-8">
<title>Payment Authorization – Order Form</title>
<link href="https://fonts.googleapis.com/css2?family=Montserrat:wght@400;500;600;700&display=swap" rel="stylesheet">
<style>
  :root {
    --brand: #1c8dbf;
    --brand-dark: #1680b1;
    --ink-blue: #1b86b8;
    --cell-tint: #ddf1f8;
    --note-tint: #d7f0f8;
    --page: #ffffff;
    --backdrop: #eceef1;
  }
  * { box-sizing: border-box; margin: 0; padding: 0; }
  html, body {
    width: 1200px; height: 912px; overflow: hidden;
    background: var(--backdrop);
    font-family: "Montserrat", sans-serif;
    color: var(--ink-blue);
  }
  .sheet {
    position: absolute; top: 192px;
    width: 408px; height: 528px;
    background: var(--page);
    box-shadow: 0 6px 18px rgba(0,0,0,0.18);
  }
  .sheet--front { left: 156px; }
  .sheet--back { left: 636px; }

  /* Header */
  .masthead { position: absolute; left: 0; top: 0; width: 408px; height: 64px; }
  .masthead__band { position: absolute; inset: 0; }
  .brand {
    position: absolute; left: 22px; top: 23px;
    display: flex; align-items: center; gap: 5px;
  }
  .brand__dot { width: 16px; height: 16px; border-radius: 50%; background: var(--brand); flex: none; }
  .brand__name {
    font-size: 12.5px; font-weight: 600; letter-spacing: -0.2px;
    color: var(--brand); white-space: nowrap;
  }
  .company {
    position: absolute; right: 24px; top: 12px;
    text-align: right; color: #fff; font-size: 7.6px; line-height: 10.3px;
    font-style: normal;
  }
  .company strong { font-weight: 700; }

  .title-band {
    position: absolute; left: 0; top: 64px; width: 408px; height: 24px;
    background: var(--brand);
    color: #fff; font-weight: 700; font-size: 9.6px; letter-spacing: 0.2px;
    display: flex; align-items: center; justify-content: center;
  }

  /* Tables */
  .form-table {
    position: absolute; left: 24px; width: 360px;
    border-collapse: collapse; table-layout: fixed;
    border: 1.4px solid var(--brand);
  }
  .form-table td, .form-table th {
    border: 1px solid var(--brand);
    font-size: 7.2px; font-weight: 600; color: var(--ink-blue);
    vertical-align: middle;
  }
  .section-head th {
    background: var(--brand); color: #fff;
    font-size: 8.4px; font-weight: 700; text-align: center;
  }
  .label-cell { background: var(--cell-tint); text-align: center; }
  .label-left { text-align: left; padding-left: 12px; }
  .choice-cell { text-align: center; vertical-align: top !important; padding-top: 6px; }

  .contact-table { top: 103px; }
  .card-table { top: 242px; }
  .order-table { top: 334px; }
  .order-table--full { top: 103px; }

  .device-cell { padding: 5px 14px; }
  .device-photo {
    width: 100%; height: 38px; border-radius: 4px;
    background: linear-gradient(135deg, #2b2f36 0%, #1a1c20 55%, #3d6f9a 100%);
  }
  .device-photo--camera { background: linear-gradient(135deg, #3a3d42 0%, #16181b 70%); }
  .device-photo--combo { background: linear-gradient(135deg, #2f5d86 0%, #22252a 50%, #121315 100%); }

  .detail-cell { padding: 3px 6px 3px 11px; vertical-align: top !important; }
  .detail-cell--centered { vertical-align: middle !important; }
  .detail__caption { text-align: center; font-weight: 600; font-size: 7px; margin-bottom: 3px; }
  .detail__title { font-weight: 700; font-size: 7px; margin-bottom: 1px; }
  .detail__line { font-weight: 400; font-size: 6.7px; line-height: 9.4px; white-space: nowrap; }

  .plan-list { list-style: none; font-weight: 700; font-size: 7px; line-height: 9.2px; }
  .plan-list li { display: flex; align-items: center; gap: 3px; }
  .plan-list li::before {
    content: ""; width: 5px; height: 5px; border: 0.8px solid #4a4a4a; flex: none;
  }
  .plan-heading { font-weight: 700; font-size: 7px; margin-bottom: 1px; }
  .top-label { vertical-align: top !important; padding: 6px 0 0 12px; text-align: left; }
  .top-center { vertical-align: top !important; padding-top: 3px; text-align: center; }
  .note-cell { background: var(--note-tint); }

  .footer-band {
    position: absolute; left: 0; bottom: 0; width: 408px; height: 19px;
    background: var(--brand); color: #fff;
    font-size: 7.2px; font-weight: 700;
    display: flex; align-items: center; justify-content: center;
  }
</style>
</head>
<body>

<!-- Front sheet -->
<section class="sheet sheet--front">
  <header class="masthead">
    <svg class="masthead__band" width="408" height="64" viewBox="0 0 408 64" aria-hidden="true">
      <polygon points="280,0 408,0 408,64 251,64" fill="var(--brand)"/>
    </svg>
    <div class="brand"><span class="brand__dot"></span><span class="brand__name">NORTHSTARTRACK</span></div>
    <address class="company">
      <strong>Northstar Track Ltd.</strong><br>
      1480 Rue Larose, Quebec<br>
      H2K 4T7 Canada<br>
      1800 555 0147
    </address>
  </header>
  <div class="title-band">PAYMENT AUTHORIZATION</div>

  <table class="form-table contact-table">
    <colgroup><col><col><col><col><col><col></colgroup>
    <tr class="section-head" style="height:19px"><th colspan="6">Customer Contact Information</th></tr>
    <tr style="height:14px">
      <td class="label-cell" colspan="2">Customer Company Name</td>
      <td class="label-cell" colspan="2">Billing Contact Name</td>
      <td class="label-cell" colspan="2">Billing E-Mail Address</td>
    </tr>
    <tr style="height:15px"><td colspan="2"></td><td colspan="2"></td><td colspan="2"></td></tr>
    <tr style="height:15px">
      <td class="label-cell" colspan="2">Billing Address</td>
      <td class="label-cell">City</td>
      <td class="label-cell">State</td>
      <td class="label-cell">Zip Code</td>
      <td class="label-cell">Phone</td>
    </tr>
    <tr style="height:14px"><td colspan="2"></td><td></td><td></td><td></td><td></td></tr>
    <tr class="section-head" style="height:19px"><th colspan="6">Payment Information</th></tr>
    <tr style="height:29px">
      <td colspan="3" style="text-align:center">Select Payment Method</td>
      <td class="choice-cell">CardOne</td>
      <td class="choice-cell">ExpressPay</td>
      <td class="choice-cell">VeroCard</td>
    </tr>
  </table>

  <table class="form-table card-table">
    <colgroup><col style="width:180px"><col></colgroup>
    <tr class="section-head" style="height:20px"><th colspan="2">PAYMENT INFORMATION – Fill only If paid by credit card</th></tr>
    <tr style="height:14px"><td class="label-left">Name on Credit Card as it Appears</td><td></td></tr>
    <tr style="height:14px"><td class="label-left">Credit Card Number</td><td></td></tr>
    <tr style="height:14px"><td class="label-left">Expiration Date</td><td></td></tr>
    <tr style="height:14px"><td class="label-left">Credit Card Billing Address</td><td></td></tr>
  </table>

  <table class="form-table order-table">
    <colgroup><col style="width:110px"><col></colgroup>
    <tr class="section-head" style="height:19px"><th colspan="2">PAYMENT INFORMATION – Fill only If paid by credit card</th></tr>
    <tr style="height:48px">
      <td class="device-cell"><div class="device-photo" role="img" aria-label="GPS tracking device product photo"></div></td>
      <td class="detail-cell">
        <p class="detail__caption">Product Order Details:</p>
        <p class="detail__title">GPS TRACKING</p>
        <p class="detail__line">GPS Tracking Devices @$199 Per unit, number of units: 10____</p>
        <p class="detail__line">Shipping &amp; Handling $19.99 Per Order. Waived on orders above $1,000</p>
      </td>
    </tr>
    <tr style="height:48px">
      <td class="device-cell"><div class="device-photo device-photo--camera" role="img" aria-label="AI dash camera product photo"></div></td>
      <td class="detail-cell detail-cell--centered">
        <p class="detail__title">AI CAMERA</p>
        <p class="detail__line">AI Camera Devices @$199 Per unit, number of units: 10____</p>
        <p class="detail__line">Shipping &amp; Handling $19.99 Per Order. Waived on orders above $1,000</p>
      </td>
    </tr>
    <tr style="height:48px">
      <td class="device-cell"><div class="device-photo device-photo--combo" role="img" aria-label="GPS tracker with AI camera bundle photo"></div></td>
      <td class="detail-cell detail-cell--centered">
        <p class="detail__title">GPS+ CAMERA</p>
        <p class="detail__line">AI Camera Devices @$199 Per unit, number of units: 10____</p>
        <p class="detail__line">Shipping &amp; Handling $19.99 Per Order. Waived on orders above $1,000</p>
      </td>
    </tr>
  </table>

  <footer class="footer-band">www.northstartrack.com</footer>
</section>

<!-- Back sheet -->
<section class="sheet sheet--back">
  <header class="masthead">
    <svg class="masthead__band" width="408" height="64" viewBox="0 0 408 64" aria-hidden="true">
      <polygon points="280,0 408,0 408,64 251,64" fill="var(--brand)"/>
    </svg>
    <div class="brand"><span class="brand__dot"></span><span class="brand__name">NORTHSTARTRACK</span></div>
    <address class="company">
      <strong>Northstar Track Ltd.</strong><br>
      1480 Rue Larose, Quebec<br>
      H2K 4T7 Canada<br>
      1800 555 0147
    </address>
  </header>
  <div class="title-band">PAYMENT AUTHORIZATION</div>

  <table class="form-table order-table--full">
    <colgroup><col style="width:111px"><col style="width:69px"><col></colgroup>
    <tr class="section-head" style="height:19px"><th colspan="3">PAYMENT INFORMATION – Fill only If paid by credit card</th></tr>
    <tr style="height:48px">
      <td class="device-cell"><div class="device-photo" role="img" aria-label="GPS tracking device product photo"></div></td>
      <td class="detail-cell" colspan="2">
        <p class="detail__caption">Product Order Details:</p>
        <p class="detail__title">GPS TRACKING</p>
        <p class="detail__line">GPS Tracking Devices @$199 Per unit, number of units: 10____</p>
        <p class="detail__line">Shipping &amp; Handling $19.99 Per Order. Waived on orders above $1,000</p>
      </td>
    </tr>
    <tr style="height:48px">
      <td class="device-cell"><div class="device-photo device-photo--camera" role="img" aria-label="AI dash camera product photo"></div></td>
      <td class="detail-cell detail-cell--centered" colspan="2">
        <p class="detail__title">AI CAMERA</p>
        <p class="detail__line">AI Camera Devices @$199 Per unit, number of units: 10____</p>
        <p class="detail__line">Shipping &amp; Handling $19.99 Per Order. Waived on orders above $1,000</p>
      </td>
    </tr>
    <tr style="height:48px">
      <td class="device-cell"><div class="device-photo device-photo--combo" role="img" aria-label="GPS tracker with AI camera bundle photo"></div></td>
      <td class="detail-cell detail-cell--centered" colspan="2">
        <p class="detail__title">GPS+ CAMERA</p>
        <p class="detail__line">AI Camera Devices @$199 Per unit, number of units: 10____</p>
        <p class="detail__line">Shipping &amp; Handling $19.99 Per Order. Waived on orders above $1,000</p>
      </td>
    </tr>
    <tr style="height:54px">
      <td class="top-label" style="padding-top:5px">Monthly Service Plan:</td>
      <td class="detail-cell" colspan="2" style="padding-top:5px">
        <p class="plan-heading">Monthly Plan: (Please check off)</p>
        <ul class="plan-list">
          <li>Base Plan, $24.99 per unit</li>
          <li>Pro Plan, $34.99 per unit</li>
          <li>ProPlus Plan, $39.99 per unit</li>
          <li>Camera Plan, $29.99 per unit</li>
        </ul>
      </td>
    </tr>
    <tr style="height:26px"><td class="top-label" colspan="3" style="padding-top:2px">Signature</td></tr>
    <tr style="height:26px">
      <td class="top-label" colspan="2" style="padding-top:3px">Printed Name</td>
      <td class="top-center">Date</td>
    </tr>
    <tr style="height:124px"><td class="top-label note-cell" colspan="3" style="padding-top:3px">NOTE</td></tr>
  </table>

  <footer class="footer-band">www.northstartrack.com</footer>
</section>

</body>
</html>
```